Educational Management System User Interface (Vantro Design Concepts)

Hi,I require a 1-page design for an educational management system. The image attached shows all required elements and also their locations. I require the design to be based on vantro-styled interfaces using elements from: http://qelvo.hostrun.io/qelvo-kitset/ & http://layoutmintly.com/layout-template/admin . Side menu's should not be too large that they hide the main content of the page.
Sorry very slight addition to the design as per new uploaded file.
I like how the elements of the vantro hub page are seperated with the background colour and white boxes. This could maybe work in the design as per the uploaded image?
Thanks,
Melvin
Reason: Some designers have some submissions.

```html
<!DOCTYPE html>
<html lang="en">
<head>
<meta charset="utf-8">
<title>Tervo LMS – Teacher Groups</title>
<link rel="stylesheet" href="https://fonts.googleapis.com/css2?family=Montserrat:wght@400;500;600&family=Arimo:wght@400;700&display=swap">
<style>
:root{
  --white:#ffffff;
  --canvas:#ececec;
  --band:#f1f1f1;
  --ink:#222222;
  --text:#333333;
  --muted:#8a8a8a;
  --blue:#5b8fc7;
  --blue-soft:#7d9fc9;
  --navy:#33466b;
  --green:#7dbb4f;
  --red:#d9433a;
  --online:#1fa21f;
  --away:#bbbbbb;
  --busy:#e2452f;
  --leave:#dde6f0;
  --photo-b:#8d6a55;
  --photo-c:#c9a58a;
  --file-tile:#c9d6e6;
}
*{box-sizing:border-box;margin:0;padding:0}
html,body{width:1200px;height:950px;overflow:hidden}
body{position:relative;background:var(--canvas);font-family:"Arimo",Arial,sans-serif;color:var(--text)}
.abs{position:absolute}
.photo{position:absolute;background:linear-gradient(160deg,var(--photo-c),var(--photo-b));border-radius:4px}

/* header */
.topbar{left:0;top:0;width:1200px;height:82px;background:var(--white);border-bottom:1px solid #cfcfcf}
.brand{left:18px;top:25px;display:flex;align-items:center;gap:10px;font-family:"Montserrat",sans-serif;font-size:26px;font-weight:500;color:var(--blue)}
.brand-dot{width:30px;height:30px;border-radius:50%;background:var(--green)}
.top-divider{left:222px;top:0;width:1px;height:72px;background:#e6e6e6}
.nav-icon{top:26px}
.tray{left:846px;top:0;width:134px;height:81px;background:#f4f4f4}
.badge{left:887px;top:24px;width:20px;height:20px;border:1px solid var(--red);border-radius:50%;background:var(--white);color:var(--red);font-size:11px;line-height:18px;text-align:center}
.user-name{left:998px;top:32px;font-family:"Montserrat",sans-serif;font-size:14px;font-weight:500;color:var(--ink)}
.user-photo{left:1133px;top:16px;width:53px;height:53px;border-radius:50%}

/* left sidebar */
.sidebar{left:0;top:82px;width:230px;height:868px;background:var(--white)}
.role{left:0;top:95px;width:230px;text-align:center;font-family:"Montserrat",sans-serif;font-size:27px;font-weight:500;color:var(--blue-soft);letter-spacing:1px}
.side-band{left:0;width:230px;height:44px;background:var(--band);padding:12px 27px;font-family:"Montserrat",sans-serif;font-size:15px;font-weight:500;color:var(--ink)}
.side-item{left:0;width:230px;height:38px;border-bottom:1px dotted #c8c8c8;padding:10px 35px;font-family:"Montserrat",sans-serif;font-size:13px;color:#555}
.side-item svg{position:absolute;right:18px;top:11px}
.btn{left:23px;width:184px;height:28px;color:var(--white);font-family:"Montserrat",sans-serif;font-size:13px;font-weight:500;text-align:center;line-height:28px;border-radius:2px}
.btn-green{background:var(--green)}
.btn-red{background:var(--red)}

/* feed */
.refine{left:740px;top:107px;width:175px;height:26px;background:var(--white);border:1px solid #cfcfcf;font-size:14px;padding:5px 8px;color:#333}
.refine-arrow{right:-1px;top:-1px;width:30px;height:26px;background:var(--blue);position:absolute}
.timeline{left:293px;top:238px;width:4px;height:712px;background:#9a9a9a}
.avatar{left:265px;width:58px;height:58px;border-radius:4px;border:1px solid #9aa;overflow:hidden}
.composer{left:340px;top:148px;width:575px;height:88px;background:#dedede}
.composer-field{position:absolute;left:13px;top:14px;width:548px;height:61px;background:var(--white);border:1px solid #ccc;padding:6px 9px;font-size:13px;color:#999}
.submit{position:absolute;left:479px;top:48px;width:72px;height:19px;background:var(--red);color:var(--white);font-size:12px;text-align:center;line-height:19px;border-radius:1px}
.post{left:340px;width:575px;background:var(--white);border:1px solid #d4d4d4}
.post::before{content:"";position:absolute;left:-9px;top:14px;border:9px solid transparent;border-left:0;border-right-color:var(--white)}
.post-name{position:absolute;left:18px;top:14px;font-size:17px;color:var(--navy)}
.post-time{position:absolute;right:11px;top:16px;font-size:13px;color:var(--muted)}
.post-time.recent{right:17px}
.post-body{position:absolute;left:18px;top:48px;width:545px;font-size:12px;line-height:15px;color:#333}
.comment-field{position:absolute;left:18px;width:543px;height:24px;border:1px solid #bdbdbd;font-size:12px;padding:5px 10px;color:#444}
.file{position:absolute;left:18px;top:108px;width:543px;height:62px;background:#f0f0f0;border:1px solid #d0d0d0}
.file-icon{position:absolute;left:11px;top:10px;width:41px;height:41px;background:var(--file-tile)}
.file-name{position:absolute;left:63px;top:9px;font-size:13px;font-weight:700;color:var(--navy)}
.file-btn{position:absolute;left:64px;top:31px;width:107px;height:18px;background:var(--green);color:var(--white);font-size:12px;font-weight:700;text-align:center;line-height:18px}
.reply{position:absolute;left:18px;width:540px}
.reply .photo{left:0;top:0;width:27px;height:29px;border-radius:2px}
.reply-name{position:absolute;left:38px;top:0;font-size:13px;font-weight:700;color:var(--navy)}
.reply-meta{font-weight:400;font-size:12px;color:var(--muted)}
.reply-text{position:absolute;left:38px;top:17px;font-size:12px;white-space:nowrap}

/* right panel */
.aside{left:947px;top:82px;width:253px;height:868px;background:var(--white);border-left:1px solid #e2e2e2}
.scroll-mark{left:1191px;top:110px;width:3px;height:100px;background:var(--blue)}
.aside-title{left:970px;font-family:"Montserrat",sans-serif;font-size:15px;font-weight:500;color:var(--navy);display:flex;align-items:center;gap:7px;letter-spacing:-0.2px}
.member{left:969px;height:36px;width:210px}
.member .photo{left:0;top:0;width:36px;height:36px}
.status{position:absolute;left:29px;top:29px;width:11px;height:11px;border-radius:50%;border:2px solid var(--white)}
.member-name{position:absolute;left:47px;top:11px;font-size:13px;font-weight:700;color:#333}
.aside-divider{left:948px;top:407px;width:252px;height:1px;background:#e4e4e4}
.event{left:969px;width:215px;height:38px}
.event .photo{left:0;top:0;width:37px;height:37px}
.event-title{position:absolute;left:47px;top:2px;font-size:13px;font-weight:700;color:#333}
.event-date{position:absolute;left:47px;top:20px;font-size:12px;font-weight:700;color:var(--muted)}
.event svg{position:absolute;left:188px;top:12px}
.leave{left:948px;top:900px;width:252px;height:37px;background:var(--leave);padding:10px 20px;font-family:"Montserrat",sans-serif;font-size:15px;font-weight:500;color:var(--navy)}
.leave svg{position:absolute;left:222px;top:13px}
</style>
</head>
<body>

<header class="abs topbar">
  <div class="abs brand"><span class="brand-dot"></span>Tervo LMS</div>
  <div class="abs top-divider"></div>
  <svg class="abs nav-icon" style="left:253px" width="34" height="30" viewBox="0 0 34 30" fill="none" stroke="#5b8fc7" stroke-width="2"><path d="M3 15 17 3l14 12"/><path d="M7 12v15h8v-8h4v8h8V12"/></svg>
  <svg class="abs nav-icon" style="left:321px;top:28px" width="30" height="28" viewBox="0 0 30 28" fill="#5b8fc7"><rect x="1" y="4" width="28" height="23" rx="1" fill="none" stroke="#5b8fc7" stroke-width="2"/><rect x="6" y="0" width="3" height="7"/><rect x="21" y="0" width="3" height="7"/><rect x="5" y="11" width="4" height="3"/><rect x="11" y="11" width="4" height="3"/><rect x="17" y="11" width="4" height="3"/><rect x="23" y="11" width="3" height="3"/><rect x="5" y="16" width="4" height="3"/><rect x="11" y="16" width="4" height="3"/><rect x="17" y="16" width="4" height="3"/><rect x="23" y="16" width="3" height="3"/><rect x="5" y="21" width="4" height="3"/><rect x="11" y="21" width="4" height="3"/></svg>
  <svg class="abs nav-icon" style="left:386px;top:26px" width="30" height="30" viewBox="0 0 30 30" fill="none" stroke="#5b8fc7" stroke-width="2"><path d="M24 14v13H2V5h16"/><path d="m7 14 5 6L27 3"/></svg>
  <svg class="abs nav-icon" style="left:450px;top:28px" width="38" height="26" viewBox="0 0 38 26" fill="none" stroke="#5b8fc7" stroke-width="2"><path d="M1 25V2h11l3 4h16v5"/><path d="M1 25 7 11h30l-6 14z" fill="#dfe9f4"/></svg>
  <div class="abs tray"></div>
  <svg class="abs" style="left:874px;top:37px" width="19" height="13" viewBox="0 0 19 13" fill="none" stroke="#8a8a8a" stroke-width="1.3"><rect x="1" y="1" width="17" height="11"/><path d="m1 1 8.5 7L18 1"/></svg>
  <div class="abs badge">2</div>
  <svg class="abs" style="left:939px;top:34px" width="15" height="17" viewBox="0 0 15 17" fill="none" stroke="#9a9a9a" stroke-width="1.3"><path d="M1 3h13M5 3V1h5v2M2.5 3l1 13h8l1-13M6 6v8M9 6v8"/></svg>
  <div class="abs user-name">Marla Quennet</div>
  <div class="photo user-photo" role="img" aria-label="Profile photo of the signed-in teacher"></div>
</header>

<nav class="abs sidebar"></nav>
<div class="abs role">TEACHER</div>
<div class="abs side-band" style="top:139px">My Groups</div>
<div class="abs side-item" style="top:184px">Group Name One<svg width="20" height="14" viewBox="0 0 20 14" fill="#6f9ccf"><path d="M0 4h11V0l9 7-9 7v-4H0z"/></svg></div>
<div class="abs side-item" style="top:222px">Group Name Two<svg width="20" height="14" viewBox="0 0 20 14" fill="#6f9ccf"><path d="M0 4h11V0l9 7-9 7v-4H0z"/></svg></div>
<div class="abs side-item" style="top:260px">Group Name Three<svg width="20" height="14" viewBox="0 0 20 14" fill="#6f9ccf"><path d="M0 4h11V0l9 7-9 7v-4H0z"/></svg></div>
<div class="abs side-item" style="top:298px">Group Name 4<svg width="20" height="14" viewBox="0 0 20 14" fill="#6f9ccf"><path d="M0 4h11V0l9 7-9 7v-4H0z"/></svg></div>
<div class="abs btn btn-green" style="top:356px">Create New Group</div>
<div class="abs btn btn-red" style="top:390px">Join More Groups</div>
<div class="abs side-band" style="top:437px">Community</div>
<div class="abs side-item" style="top:481px">Study Finch<svg width="20" height="14" viewBox="0 0 20 14" fill="#6f9ccf"><path d="M0 4h11V0l9 7-9 7v-4H0z"/></svg></div>

<main>
  <div class="abs refine">Refine by Group<span class="refine-arrow"><svg width="30" height="26" viewBox="0 0 30 26"><path d="M10 10h10l-5 6z" fill="#fff"/></svg></span></div>
  <div class="abs timeline"></div>

  <div class="abs avatar" style="top:148px;background:#7a9cc6"><svg width="58" height="58" viewBox="0 0 58 58" fill="#fff"><circle cx="29" cy="22" r="11"/><path d="M8 58c0-14 9-21 21-21s21 7 21 21z"/></svg></div>
  <svg class="abs" style="left:284px;top:220px" width="22" height="22" viewBox="0 0 22 22" fill="none" stroke="#8d8d8d" stroke-width="2.5"><path d="M17 6a8 8 0 1 1-10 0"/><path d="M11 2v6"/></svg>
  <div class="abs composer">
    <div class="composer-field">Write new post...
      <svg style="position:absolute;left:465px;top:7px" width="72" height="16" viewBox="0 0 72 16" fill="none" stroke="#555" stroke-width="1.2"><path d="M3 12l8-8a2.5 2.5 0 0 1 3.5 3.5L7 15M6 9l4-4"/><path d="M26 1h6l4 4v10H26z M32 1v4h4"/><rect x="51" y="4" width="20" height="11" rx="1"/><circle cx="61" cy="9.5" r="3.5"/><path d="M56 4l2-3h6l2 3"/></svg>
    </div>
    <div class="submit">Submit</div>
  </div>

  <div class="avatar photo" style="top:254px" role="img" aria-label="Photo of post author"></div>
  <article class="abs post" style="top:264px;height:150px">
    <div class="post-name">John Doe</div>
    <div class="post-time recent">22 min ago</div>
    <p class="post-body">Lorem Ipsum is simply dummy text of the printing and typesetting industry. Lorem Ipsum has been the industry's standard dummy text ever since the 1500s, when an unknown printer took a galley of type and scrambled it to make a type specimen book.</p>
    <div class="comment-field" style="top:109px">Add a comment...</div>
  </article>

  <div class="avatar photo" style="top:433px;background:linear-gradient(160deg,#a07e62,#6f5544)" role="img" aria-label="Photo of post author"></div>
  <article class="abs post" style="top:443px;height:326px">
    <div class="post-name">John Doe</div>
    <div class="post-time">09:15 &nbsp;10/05/2014</div>
    <p class="post-body">Lorem Ipsum is simply dummy text of the printing and typesetting industry. Lorem Ipsum has been the industry's standard dummy text ever since the 1500s, when an unknown printer took a galley of type and scrambled it to make a type specimen book.</p>
    <div class="file">
      <div class="file-icon"><svg width="41" height="41" viewBox="0 0 41 41" fill="none" stroke="#4a6a92" stroke-width="1.6"><path d="M13 8h11l5 5v20H13z"/><path d="M24 8v5h5"/><path d="M16.5 19h9M16.5 23h9M16.5 27h6"/></svg></div>
      <div class="file-name">Result.pdf - 1.4MB</div>
      <div class="file-btn">Download file</div>
    </div>
    <div class="reply" style="top:187px">
      <div class="photo" role="img" aria-label="Photo of commenter"></div>
      <div class="reply-name">John P <span class="reply-meta">&nbsp;| &nbsp;09:15 &nbsp;11/05/2014</span></div>
      <div class="reply-text">Lorem Ipsum is simply dummy text of the printing and typesetting in dustry.</div>
    </div>
    <div class="reply" style="top:235px">
      <div class="photo" role="img" aria-label="Photo of commenter"></div>
      <div class="reply-name">Tobin Reyle <span class="reply-meta">&nbsp;| &nbsp;09:15 &nbsp;14/05/2014</span></div>
      <div class="reply-text">Lorem Ipsum is simply dummy text</div>
    </div>
    <div class="comment-field" style="top:286px">Add a comment...</div>
  </article>

  <div class="avatar photo" style="top:788px" role="img" aria-label="Photo of post author"></div>
  <article class="abs post" style="top:798px;height:150px">
    <div class="post-name">John Doe</div>
    <div class="post-time">09:15 &nbsp;14/05/2014</div>
    <p class="post-body">Lorem Ipsum is simply dummy text of the printing and typesetting industry. Lorem Ipsum has been the industry's standard dummy text ever since the 1500s, when an unknown printer took a galley of type and scrambled it to make a type specimen book.</p>
    <div class="comment-field" style="top:109px">Add a comment...</div>
  </article>
</main>

<aside class="abs aside"></aside>
<div class="abs scroll-mark"></div>
<div class="abs aside-title" style="top:106px"><svg width="26" height="18" viewBox="0 0 26 18" fill="#9fb6d4"><circle cx="8" cy="5" r="4"/><path d="M0 18c0-6 3-8 8-8s8 2 8 8z"/><circle cx="17" cy="4" r="3.5"/><path d="M15 9c6 0 10 2 10 8h-7c0-3-1-6-3-8z"/></svg>Group Members</div>
<div class="abs member" style="top:141px"><div class="photo" style="background:linear-gradient(160deg,#ddd,#888)" role="img" aria-label="Member photo"></div><span class="status" style="background:var(--online)"></span><div class="member-name">John Doe</div></div>
<div class="abs member" style="top:194px"><div class="photo" style="background:linear-gradient(160deg,#7a3a4a,#3a2028)" role="img" aria-label="Member photo"></div><span class="status" style="background:var(--online)"></span><div class="member-name">Lorem Ipsum</div></div>
<div class="abs member" style="top:245px"><div class="photo" style="background:linear-gradient(160deg,#8a6a55,#4a3a30)" role="img" aria-label="Member photo"></div><span class="status" style="background:var(--away)"></span><div class="member-name">Idris Palvane</div></div>
<div class="abs member" style="top:298px"><div class="photo" style="background:linear-gradient(160deg,#e8c8b0,#b07050)" role="img" aria-label="Member photo"></div><span class="status" style="background:var(--busy)"></span><div class="member-name">Palvane Studio</div></div>
<div class="abs member" style="top:350px"><div class="photo" style="background:linear-gradient(160deg,#e0c8a8,#a87a58)" role="img" aria-label="Member photo"></div><span class="status" style="background:var(--online)"></span><div class="member-name">Palvane Studio</div></div>
<div class="abs aside-divider"></div>
<div class="abs aside-title" style="top:429px"><svg width="15" height="15" viewBox="0 0 15 15" fill="#9fb6d4"><rect x="0" y="2" width="15" height="13"/><rect x="3" y="0" width="2" height="4"/><rect x="10" y="0" width="2" height="4"/><g fill="#fff"><rect x="2" y="6" width="2" height="2"/><rect x="6" y="6" width="2" height="2"/><rect x="10" y="6" width="2" height="2"/><rect x="2" y="10" width="2" height="2"/><rect x="6" y="10" width="2" height="2"/><rect x="10" y="10" width="2" height="2"/></g></svg>UpComing Group Events</div>

<div class="abs event" style="top:463px"><div class="photo" style="background:linear-gradient(160deg,#7a8ea8,#3a4a5a)" role="img" aria-label="Event member photo"></div><div class="event-title">Orlena has joined</div><div class="event-date">Mar 06, 2014</div><svg width="22" height="19" viewBox="0 0 22 19"><path d="M11 0 22 19H0z" fill="#8fb0d4"/><rect x="10" y="6" width="2" height="7" fill="#fff"/><rect x="10" y="14.5" width="2" height="2" fill="#fff"/></svg></div>
<div class="abs event" style="top:524px"><div class="photo" style="background:linear-gradient(160deg,#8a7060,#3a3028)" role="img" aria-label="Event member photo"></div><div class="event-title">Orlena has joined</div><div class="event-date">Mar 06, 2014</div><svg width="22" height="19" viewBox="0 0 22 19"><path d="M11 0 22 19H0z" fill="#8fb0d4"/><rect x="10" y="6" width="2" height="7" fill="#fff"/><rect x="10" y="14.5" width="2" height="2" fill="#fff"/></svg></div>
<div class="abs event" style="top:586px"><div class="photo" style="background:linear-gradient(160deg,#d8c8c0,#9a7a68)" role="img" aria-label="Event member photo"></div><div class="event-title">Brightmill</div><div class="event-date">Mar 06, 2014</div><svg width="22" height="19" viewBox="0 0 22 19"><path d="M11 0 22 19H0z" fill="#8fb0d4"/><rect x="10" y="6" width="2" height="7" fill="#fff"/><rect x="10" y="14.5" width="2" height="2" fill="#fff"/></svg></div>
<div class="abs event" style="top:648px"><div class="photo" style="background:#e3212b" role="img" aria-label="Studio avatar"></div><div class="event-title">Norrow Lab</div><div class="event-date">Mar 06, 2014</div><svg width="22" height="19" viewBox="0 0 22 19"><path d="M11 0 22 19H0z" fill="#8fb0d4"/><rect x="10" y="6" width="2" height="7" fill="#fff"/><rect x="10" y="14.5" width="2" height="2" fill="#fff"/></svg></div>
<div class="abs event" style="top:709px"><div class="photo" style="background:linear-gradient(160deg,#6ac8c8,#c08870)" role="img" aria-label="Event member photo"></div><div class="event-title">Korvel Brand</div><div class="event-date">Mar 06, 2014</div><svg width="22" height="19" viewBox="0 0 22 19"><path d="M11 0 22 19H0z" fill="#8fb0d4"/><rect x="10" y="6" width="2" height="7" fill="#fff"/><rect x="10" y="14.5" width="2" height="2" fill="#fff"/></svg></div>
<div class="abs event" style="top:771px"><div class="photo" style="background:linear-gradient(160deg,#e8b070,#a06a48)" role="img" aria-label="Event member photo"></div><div class="event-title">Orlena has joined</div><div class="event-date">Mar 06, 2014</div><svg width="22" height="19" viewBox="0 0 22 19"><path d="M11 0 22 19H0z" fill="#8fb0d4"/><rect x="10" y="6" width="2" height="7" fill="#fff"/><rect x="10" y="14.5" width="2" height="2" fill="#fff"/></svg></div>
<div class="abs event" style="top:833px"><div class="photo" style="background:linear-gradient(160deg,#6a4a3a,#2a1a18)" role="img" aria-label="Event member photo"></div><div class="event-title">Orlena has joined</div><div class="event-date">Mar 06, 2014</div><svg width="22" height="19" viewBox="0 0 22 19"><path d="M11 0 22 19H0z" fill="#8fb0d4"/><rect x="10" y="6" width="2" height="7" fill="#fff"/><rect x="10" y="14.5" width="2" height="2" fill="#fff"/></svg></div>

<div class="abs leave">Request to Leave Group<svg width="7" height="10" viewBox="0 0 7 10"><path d="M0 0l7 5-7 5z" fill="#33466b"/></svg></div>

</body>
</html>
```